Cybersecurity Start-Up - Veloriq

We need a MS Word Template for everyday documents. This would be leveraged to create reports, marketing materials, internal memos etc.

The document should follow the standard MS Word template format and have an H1,H2,H3, paragraph, Title, bold font, regular font, table etc. All editable with normal MS Word features.

Our logo is also attached. We would like to see the same color scheme used throughout the document. Additional attached is a sample word document that outlines all of the components we would like to see in the template.

Requirements
Must have
• - Submission must meet all standard MS Word Template requirements.
• - Submission should make use of Built in MS Styles so as the user of the template I should be able to create a brand new page and insert an H1 for example and be able to select from the styles drop down the same font/color/style that you have designed for your submission.
• - All sections in the provided document need to be contained in your submission.
• - The table of contents should auto update if I add a new page, heading, section etc.
• - Need to read and understand all of my comments which I have placed in the sample document uploaded to the briefing
Should not have
• no fixed textboxes or image boxes. everything needs to be smoothly editable in MS Word. "Editable" means more than just being able to alter text.

```html
<!DOCTYPE html>
<html lang="en">
<head>
<meta charset="utf-8">
<title>Veloriq document template pages</title>
<link href="https://fonts.googleapis.com/css2?family=Montserrat:wght@400;500;600;700&display=swap" rel="stylesheet">
<style>
:root{
  --navy:#0a2a6c;
  --navy-deep:#061a4a;
  --orange:#f08a24;
  --orange-soft:#fbd3a6;
  --red-orange:#e8572e;
  --ink:#3a3a3a;
  --body:#6a6a6a;
  --rule:#d9d9d9;
  --bar:#3d3d3d;
  --canvas:#ffffff;
}
*{box-sizing:border-box;margin:0;padding:0}
html,body{width:846px;height:1200px;overflow:hidden;background:var(--canvas)}
body{position:relative;font-family:"Montserrat",Arial,sans-serif}
.page{position:absolute;width:203px;height:291px;background:#fff;overflow:hidden;box-shadow:0 0 3px rgba(0,0,0,.25)}
.col1{left:6px}.col2{left:216px}.col3{left:427px}.col4{left:638px}
.row1{top:7px}.row2{top:305px}.row3{top:604px}.row4{top:903px}

.page-title{position:absolute;left:23px;top:30px;font-size:9.5px;font-weight:500;color:var(--ink)}
.content{position:absolute;left:23px;right:23px;top:64px;font-size:2.6px;line-height:3.4px;color:var(--body)}
.content p{margin-bottom:3px}
.h2{color:var(--red-orange);font-size:3.6px;font-weight:600;margin:5px 0 2px}
.h3{color:var(--ink);font-size:3.2px;font-weight:600;margin:3px 0 1px}
.footer{position:absolute;left:0;bottom:0;width:100%;height:7px;background:var(--bar)}
.footer::after{content:"";position:absolute;left:50%;top:-2px;width:7px;height:7px;margin-left:-3.5px;background:var(--orange);transform:rotate(45deg)}

/* covers */
.cover{background:linear-gradient(160deg,#0c3384 0%,var(--navy) 45%,var(--navy-deep) 100%)}
.cover-art{position:absolute;inset:0;background:radial-gradient(circle at 65% 45%,rgba(90,150,230,.35),rgba(10,42,108,0) 60%)}
.cover-title{position:absolute;left:24px;top:32px;font-size:12.5px;font-weight:600;color:#fff}
.brand{position:absolute;right:24px;bottom:38px;display:flex;align-items:center;gap:4px;font-size:12px;font-weight:600;color:#fff}
.brand-mark{width:7px;height:7px;border-radius:50%;background:var(--orange)}
.cover-date{position:absolute;left:24px;bottom:7px;font-size:3px;color:#c8d3ea}
.contact{position:absolute;left:24px;top:30px;font-size:3.4px;line-height:5px;color:#fff}
.contact-name{color:var(--orange);font-size:6px;font-weight:600;margin-bottom:3px}
.contact-lines{padding-left:10px}

/* toc */
.toc{list-style:none;top:78px}
.toc li{display:flex;justify-content:space-between;font-size:3.3px;line-height:8.7px;color:var(--body)}
.toc li.sub{padding-left:8px}
.toc li.sub2{padding-left:16px}

/* tables */
table{width:100%;border-collapse:collapse;font-size:2.5px;color:var(--body)}
td{padding:.8px 1px;vertical-align:top}
.tbl-lined tr{border-bottom:.3px solid var(--rule)}
.tbl-lined .tbl-cap{border-bottom:.6px solid var(--red-orange);color:var(--ink);font-weight:600}
.module{margin-bottom:10px}
.module .end{border-bottom:.6px solid var(--orange)}
.tbl-orange .cap td{background:var(--red-orange);color:#fff}
.tbl-orange .head td{background:var(--orange-soft);color:var(--ink)}
.tbl-orange{border:.4px solid var(--red-orange);margin-bottom:4px}
.tbl-sum .cap td{background:var(--orange);color:#fff}
.tbl-sum .head td{background:var(--orange-soft)}
.sev{display:inline-block;width:3px;height:3px;border-radius:50%;vertical-align:middle;margin-right:4px}
.sev-critical{background:#e5141b}
.sev-high{background:conic-gradient(#f08a24 0 75%,#f7c48a 0)}
.sev-medium{background:conic-gradient(#1e8fd6 0 50%,#bfe1f6 0)}
.sev-low{background:conic-gradient(#5aae3c 0 25%,#cfe8c4 0)}
.t-crit{color:#e5141b}.t-high{color:#f08a24}.t-med{color:#1e8fd6}.t-low{color:#5aae3c}

/* finding cards */
.finding{border:.4px solid #9a9a9a;margin-bottom:5px;font-size:2.5px;line-height:3.2px;color:var(--body)}
.finding-head{background:var(--bar);color:#fff;font-weight:600;padding:1.5px 2px;position:relative;height:10px;line-height:3px}
.finding-head .sev{position:absolute;right:2px;top:2px;width:6px;height:6px;border:.4px solid #fff}
.finding-row{display:flex;border-top:.3px solid var(--rule)}
.finding-row .label{width:62px;padding:2px;display:flex;align-items:center}
.finding-row .value{flex:1;padding:2px}
.finding ul{padding-left:4px}
.evidence{width:40px;height:58px;margin:2px 0;background:linear-gradient(#f4f4f4,#dedede);border:.3px solid #bbb}
.assets{list-style:disc;padding-left:4px}
</style>
</head>
<body>

<!-- Cover A -->
<section class="page cover col1 row1">
  <div class="cover-art" role="img" aria-label="Blue digital network background"></div>
  <h1 class="cover-title">Project title goes here</h1>
  <div class="brand"><span class="brand-mark"></span>Veloriq</div>
  <div class="cover-date">DD/MM/YYYY</div>
</section>

<!-- Cover B -->
<section class="page cover col2 row1">
  <div class="cover-art" role="img" aria-label="Blue background with a hand touching a digital padlock"></div>
  <h1 class="cover-title">Project title goes here</h1>
  <div class="brand"><span class="brand-mark"></span>Veloriq</div>
  <div class="cover-date">DD/MM/YYYY</div>
</section>

<!-- Table of contents -->
<section class="page col3 row1">
  <h2 class="page-title">Table of contents</h2>
  <ul class="content toc">
    <li><span>Table of contents</span><span>03</span></li>
    <li><span>Subject introduction</span><span>04</span></li>
    <li class="sub"><span>Subjects recommended</span><span>04</span></li>
    <li class="sub"><span>Professional outcomes</span><span>04</span></li>
    <li><span>Training content</span><span>05</span></li>
    <li><span>Technical overview</span><span>06</span></li>
    <li class="sub"><span>Severity ratings</span><span>06</span></li>
    <li class="sub"><span>Summary of findings</span><span>07</span></li>
    <li class="sub"><span>Detailed observations</span><span>07</span></li>
    <li class="sub2"><span>Critical findings</span><span>07</span></li>
    <li class="sub2"><span>High findings</span><span>08</span></li>
    <li class="sub2"><span>Medium findings</span><span>09</span></li>
    <li class="sub2"><span>Low findings</span><span>10</span></li>
    <li><span>Appendix 01</span><span>11</span></li>
    <li class="sub"><span>Engagement methodology</span><span>11</span></li>
  </ul>
  <div class="footer"></div>
</section>

<!-- Subject introduction -->
<section class="page col4 row1">
  <h2 class="page-title">Subject introduction</h2>
  <div class="content">
    <p>This paragraph uses the standard body style of the template. Replace it with the content of the section, keeping sentences short and clear. Headings, lists and tables above and below follow the same styles, so new pages keep the look of the document without any manual formatting.</p>
    <div class="h2">Subject recommended</div>
    <p>This paragraph uses the standard body style of the template. Replace it with the content of the section, keeping sentences short and clear. Headings, lists and tables above and below follow the same styles, so new pages keep the look of the document without any manual formatting.</p>
    <div class="h2">Professional outcomes</div>
    <table class="tbl-lined">
      <tr><td class="tbl-cap" colspan="2">Work Roles – Table 1</td></tr>
      <tr><td colspan="2">Work Role Name</td></tr>
      <tr><td colspan="2">Specialty Area</td></tr>
      <tr><td colspan="2">CSF Category</td></tr>
      <tr><td colspan="2">Work Role Description</td></tr>
      <tr><td>Tasks</td><td>This is task 1<br>This is task 2</td></tr>
      <tr><td>Skills</td><td>This is skill 1<br>This is skill 2</td></tr>
      <tr><td>Abilities</td><td>This is ability 1<br>This is ability 2</td></tr>
    </table>
  </div>
  <div class="footer"></div>
</section>

<!-- Training content -->
<section class="page col1 row2">
  <h2 class="page-title">Training content</h2>
  <div class="content" style="top:66px">
    <table class="tbl-lined module"><tr><td class="tbl-cap" colspan="2">Module 1 – Table 2</td></tr><tr><td>Name</td><td>Week</td></tr><tr><td colspan="2">Module Description</td></tr><tr><td colspan="2">Acquired Competences</td></tr><tr><td colspan="2">Deliverables</td></tr><tr class="end"><td colspan="2">Assessment system</td></tr></table>
    <table class="tbl-lined module"><tr><td class="tbl-cap" colspan="2">Module 2 – Table 2</td></tr><tr><td>Name</td><td>Week</td></tr><tr><td colspan="2">Module Description</td></tr><tr><td colspan="2">Acquired Competences</td></tr><tr><td colspan="2">Deliverables</td></tr><tr class="end"><td colspan="2">Assessment system</td></tr></table>
    <table class="tbl-lined module"><tr><td class="tbl-cap" colspan="2">Module 3 – Table 2</td></tr><tr><td>Name</td><td>Week</td></tr><tr><td colspan="2">Module Description</td></tr><tr><td colspan="2">Acquired Competences</td></tr><tr><td colspan="2">Deliverables</td></tr><tr class="end"><td colspan="2">Assessment system</td></tr></table>
    <table class="tbl-lined module"><tr><td class="tbl-cap" colspan="2">Module 4 – Table 2</td></tr><tr><td>Name</td><td>Week</td></tr><tr><td colspan="2">Module Description</td></tr><tr><td colspan="2">Acquired Competences</td></tr><tr><td colspan="2">Deliverables</td></tr><tr class="end"><td colspan="2">Assessment system</td></tr></table>
  </div>
  <div class="footer"></div>
</section>

<!-- Technical overview: severity -->
<section class="page col2 row2">
  <h2 class="page-title">Technical overview</h2>
  <div class="content" style="top:66px">
    <p>This paragraph uses the standard body style of the template. Replace it with the content of the section, keeping sentences short and clear. Headings, lists and tables above and below follow the same styles, so new pages keep the look of the document without any manual formatting.</p>
    <table class="tbl-orange">
      <tr class="cap"><td colspan="2">Table 3</td></tr>
      <tr class="head"><td>Sub heading 1</td><td>Sub heading 2</td></tr>
      <tr><td>Target 1</td><td>Solution 1</td></tr>
      <tr><td>Target 2</td><td>Solution 2</td></tr>
    </table>
    <div class="h2">Severity rating</div>
    <div class="h3">Critical</div><p>This paragraph uses the standard body style of the template. Replace it with the content of the section, keeping sentences short and clear. Headings, lists and tables above and below follow the same styles, so new pages keep the look of the document without any manual formatting.</p>
    <div class="h3">High</div><p>This paragraph uses the standard body style of the template. Replace it with the content of the section, keeping sentences short and clear. Headings, lists and tables above and below follow the same styles, so new pages keep the look of the document without any manual formatting.</p>
    <div class="h3">Medium</div><p>This paragraph uses the standard body style of the template. Replace it with the content of the section, keeping sentences short and clear. Headings, lists and tables above and below follow the same styles, so new pages keep the look of the document without any manual formatting.</p>
    <div class="h3">Low</div><p>This paragraph uses the standard body style of the template. Replace it with the content of the section, keeping sentences short and clear. Headings, lists and tables above and below follow the same styles, so new pages keep the look of the document without any manual formatting.</p>
  </div>
  <div class="footer"></div>
</section>

<!-- Technical overview: summary + critical -->
<section class="page col3 row2">
  <h2 class="page-title">Technical overview</h2>
  <div class="content" style="top:62px">
    <div class="h2" style="margin-top:0">Summary of findings</div>
    <p>This paragraph uses the standard body style of the template. Replace it with the content of the section, keeping sentences short and clear. Headings, lists and tables above and below follow the same styles, so new pages keep the look of the document without any manual formatting.</p>
    <table class="tbl-sum tbl-orange" style="border-color:var(--orange)">
      <tr class="cap"><td colspan="2">Table 4</td></tr>
      <tr class="head"><td>Finding Name</td><td>Severity</td></tr>
      <tr><td>Critical Finding Title</td><td><span class="sev sev-critical"></span><span class="t-crit">Critical</span></td></tr>
      <tr><td>High Finding Title</td><td><span class="sev sev-high"></span><span class="t-high">High</span></td></tr>
      <tr><td>Medium Finding Title</td><td><span class="sev sev-medium"></span><span class="t-med">Medium</span></td></tr>
      <tr><td>Low Finding Title</td><td><span class="sev sev-low"></span><span class="t-low">Low</span></td></tr>
    </table>
    <div class="h2">Detailed observation</div>
    <div class="h3">Critical findings</div>
    <div class="finding">
      <div class="finding-head">Insecure configurations<br>identified<span class="sev sev-critical"></span></div>
      <div class="finding-row"><div class="label">Observation</div><div class="value">This paragraph uses the standard body style of the template. Replace it with the content of the section, keeping sentences short and clear. Headings, lists and tables above and below follow the same styles, so new pages keep the look of the document without any manual formatting.</div></div>
      <div class="finding-row"><div class="label">Evidence</div><div class="value"><div class="evidence" role="img" aria-label="Screenshot of a report page as evidence"></div></div></div>
    </div>
  </div>
  <div class="footer"></div>
</section>

<!-- Technical overview: high -->
<section class="page col4 row2">
  <h2 class="page-title">Technical overview</h2>
  <div class="content" style="top:70px">
    <div class="finding">
      <div class="finding-head">Insecure configurations<br>identified<span class="sev sev-critical"></span></div>
      <div class="finding-row"><div class="label">Recommendation</div><div class="value">This paragraph uses the standard body style of the template. Replace it with the content of the section, keeping sentences short and clear. Headings, lists and tables above and below follow the same styles, so new pages keep the look of the document without any manual formatting.<ul><li>Apply the fix listed.</li><li>Apply the fix listed.</li></ul></div></div>
      <div class="finding-row"><div class="label">Assets Affected</div><div class="value"><ul class="assets"><li>127.0.0.1</li><li>127.0.0.2</li><li>127.0.0.3</li></ul></div></div>
    </div>
    <div class="h3">High findings</div>
    <div class="finding">
      <div class="finding-head">Insecure configurations<br>identified<span class="sev sev-high"></span></div>
      <div class="finding-row"><div class="label">Observation</div><div class="value">This paragraph uses the standard body style of the template. Replace it with the content of the section, keeping sentences short and clear. Headings, lists and tables above and below follow the same styles, so new pages keep the look of the document without any manual formatting.</div></div>
      <div class="finding-row"><div class="label">Evidence</div><div class="value"><div class="evidence" role="img" aria-label="Screenshot of a report page as evidence"></div></div></div>
    </div>
  </div>
  <div class="footer"></div>
</section>

<!-- Technical overview: medium -->
<section class="page col1 row3">
  <h2 class="page-title">Technical overview</h2>
  <div class="content" style="top:71px">
    <div class="finding">
      <div class="finding-head">Insecure configurations<br>identified<span class="sev sev-high"></span></div>
      <div class="finding-row"><div class="label">Recommendation</div><div class="value">This paragraph uses the standard body style of the template. Replace it with the content of the section, keeping sentences short and clear. Headings, lists and tables above and below follow the same styles, so new pages keep the look of the document without any manual formatting.<ul><li>Apply the fix listed.</li><li>Apply the fix listed.</li></ul></div></div>
      <div class="finding-row"><div class="label">Assets Affected</div><div class="value"><ul class="assets"><li>127.0.0.1</li><li>127.0.0.2</li><li>127.0.0.3</li></ul></div></div>
    </div>
    <div class="h3">Medium findings</div>
    <div class="finding">
      <div class="finding-head">Insecure configurations<br>identified<span class="sev sev-medium"></span></div>
      <div class="finding-row"><div class="label">Observation</div><div class="value">This paragraph uses the standard body style of the template. Replace it with the content of the section, keeping sentences short and clear. Headings, lists and tables above and below follow the same styles, so new pages keep the look of the document without any manual formatting.</div></div>
      <div class="finding-row"><div class="label">Evidence</div><div class="value"><div class="evidence" role="img" aria-label="Screenshot of a report page as evidence"></div></div></div>
    </div>
  </div>
  <div class="footer"></div>
</section>

<!-- Technical overview: low -->
<section class="page col2 row3">
  <h2 class="page-title">Technical overview</h2>
  <div class="content" style="top:71px">
    <div class="finding">
      <div class="finding-head">Insecure configurations<br>identified<span class="sev sev-medium"></span></div>
      <div class="finding-row"><div class="label">Recommendation</div><div class="value">This paragraph uses the standard body style of the template. Replace it with the content of the section, keeping sentences short and clear. Headings, lists and tables above and below follow the same styles, so new pages keep the look of the document without any manual formatting.<ul><li>Apply the fix listed.</li><li>Apply the fix listed.</li></ul></div></div>
      <div class="finding-row"><div class="label">Assets Affected</div><div class="value"><ul class="assets"><li>127.0.0.1</li><li>127.0.0.2</li><li>127.0.0.3</li></ul></div></div>
    </div>
    <div class="h3">Low findings</div>
    <div class="finding">
      <div class="finding-head">Insecure configurations<br>identified<span class="sev sev-low"></span></div>
      <div class="finding-row"><div class="label">Observation</div><div class="value">This paragraph uses the standard body style of the template. Replace it with the content of the section, keeping sentences short and clear. Headings, lists and tables above and below follow the same styles, so new pages keep the look of the document without any manual formatting.</div></div>
      <div class="finding-row"><div class="label">Evidence</div><div class="value"><div class="evidence" role="img" aria-label="Screenshot of a report page as evidence"></div></div></div>
    </div>
  </div>
  <div class="footer"></div>
</section>

<!-- Appendix -->
<section class="page col3 row3">
  <h2 class="page-title">Appendix 01</h2>
  <div class="content" style="top:62px">
    <div class="h2" style="margin-top:0">Engagement methodology</div>
    <p>This paragraph uses the standard body style of the template. Replace it with the content of the section, keeping sentences short and clear. Headings, lists and tables above and below follow the same styles, so new pages keep the look of the document without any manual formatting.</p>
  </div>
  <div class="footer"></div>
</section>

<!-- Back cover A -->
<section class="page cover col4 row3">
  <div class="cover-art" role="img" aria-label="Blue digital network background"></div>
  <div class="contact">
    <div class="contact-name">Mara Ellison</div>
    <div class="contact-lines">000.000.000.000<br>mara@veloriq.com<br>www.veloriq.com<br>#, Lorem Ipsum, Lorem Ipsum</div>
  </div>
  <div class="brand"><span class="brand-mark"></span>Veloriq</div>
  <div class="cover-date">DD/MM/YYYY</div>
</section>

<!-- Back cover B -->
<section class="page cover col1 row4">
  <div class="cover-art" role="img" aria-label="Blue background with a hand touching a digital padlock"></div>
  <div class="contact">
    <div class="contact-name">Mara Ellison</div>
    <div class="contact-lines">000.000.000.000<br>mara@veloriq.com<br>www.veloriq.com<br>#, Lorem Ipsum, Lorem Ipsum</div>
  </div>
  <div class="brand"><span class="brand-mark"></span>Veloriq</div>
  <div class="cover-date">DD/MM/YYYY</div>
</section>

</body>
</html>
```